Fast Business Card Project

I need a business card with the name RENATO DUARTE stylized on one side and my email on the other (renatocosta4711@mailnova.com)

Industry/Entity Type

Business

Contact Information for Business Card

www.trilhamar.com.br

```html
<!DOCTYPE html>
<html lang="en">
<head>
<meta charset="utf-8">
<title>Renato Duarte — Business Card</title>
<link href="https://fonts.googleapis.com/css2?family=Open+Sans:wght@400;700&family=Arimo:wght@400&display=swap" rel="stylesheet">
<style>
  :root {
    --page-bg: #ffffff;
    --card-bg: #000000;
    --text-light: #ffffff;
    --mark-light: #bdbdbd;
    --mark-faint: #2a2a2a;
    --shadow: rgba(0, 0, 0, 0.35);
  }
  * { margin: 0; padding: 0; box-sizing: border-box; }
  html, body {
    width: 1200px;
    height: 1016px;
    overflow: hidden;
    background: var(--page-bg);
  }
  .sheet {
    position: relative;
    width: 1200px;
    height: 1016px;
  }
  .card {
    position: absolute;
    left: 313px;
    width: 573px;
    height: 327px;
    background: var(--card-bg);
    box-shadow: 6px 9px 12px var(--shadow);
  }
  .card--front { top: 114px; }
  .card--back { top: 529px; }

  .front__mark {
    position: absolute;
    left: 42px;
    top: 58px;
    font-family: "Open Sans", sans-serif;
    font-weight: 700;
    font-size: 72px;
    line-height: 1;
    letter-spacing: 2px;
    color: var(--mark-light);
  }
  .front__name {
    position: absolute;
    left: 37px;
    top: 225px;
    font-family: "Open Sans", sans-serif;
    font-size: 37px;
    line-height: 1;
    color: var(--text-light);
    white-space: nowrap;
  }
  .front__name-first { font-weight: 700; }
  .front__name-last { font-weight: 400; margin-left: 4px; }
  .front__email {
    position: absolute;
    left: 38px;
    top: 265px;
    font-family: "Arimo", Arial, sans-serif;
    font-size: 16px;
    letter-spacing: 1.6px;
    line-height: 1;
    color: var(--text-light);
  }

  .back__mark {
    position: absolute;
    left: 0;
    right: 0;
    top: 48px;
    text-align: center;
    font-family: "Open Sans", sans-serif;
    font-weight: 700;
    font-size: 160px;
    line-height: 1;
    letter-spacing: 6px;
    color: var(--mark-faint);
  }
  .back__web {
    position: absolute;
    left: 0;
    right: 0;
    top: 248px;
    text-align: center;
    font-family: "Open Sans", sans-serif;
    font-weight: 400;
    font-size: 27px;
    line-height: 1;
    color: var(--text-light);
  }
</style>
</head>
<body>
  <main class="sheet">
    <section class="card card--front" aria-label="Card front">
      <div class="front__mark">RD</div>
      <h1 class="front__name"><span class="front__name-first">RENATO</span><span class="front__name-last">DUARTE</span></h1>
      <p class="front__email">renatocosta4711@mailnova.com</p>
    </section>
    <section class="card card--back" aria-label="Card back">
      <div class="back__mark">RD</div>
      <p class="back__web">www.trilhamar.com.br</p>
    </section>
  </main>
</body>
</html>
```